Corporate Financing/Banking Website Design

I need a website for a corporate financing website.

The company helps other companies raise money for financing.

Content for the website can be found here: https://www.pinemoor.ca/northbaycapital/

Each section from the content in the main page above should have a corresponding image associated with each "Section"

1. Financing solutions that will be provided by Tarnwell Ridge Capital will include:

2. The financing solutions mentioned above will assist businesses to:

3. The industry sectors focussed on are, but not limited to:

We need to make sure that the website has clear buttons for the visitor to "Apply Now" and "Book an Appointment" to apply for financing options.

We need the following pages designed
Home
About Us
Financing Solutions
Contact Us.

For the Logo:

The company name is Tarnwell Ridge Capital. Something that emphasizes direction and progress and is related to Corporate finance

Something professional that conveys confidence

Target Market(s)

Corporation and large business

Logo Text

Tarnwell Ridge Capital

Number of Pages Required

4 page

Colors
0393ce

Requirements
Must have
• Use the color: #OA64BC

Please ensure 'Apply Now' & 'Book an Appointment' buttons are very clear and placed appropriately on the webpage.

In the Footer I would like 'T&C's' and 'Privacy Policy' links

Social Media icon links will be 'LinkedIn / Facebook/ Twitter and we should keep these in Footer and Contacts page section.
Should not have
• - Do not include a search field

```html
<!DOCTYPE html>
<html lang="en">
<head>
<meta charset="utf-8">
<title>Tarnwell Ridge Capital — Corporate Financing</title>
<link rel="stylesheet" href="https://fonts.googleapis.com/css2?family=IBM+Plex+Sans:wght@400;500;600;700&family=Open+Sans:wght@400;600&display=swap">
<style>
:root{
  --brand:#0393ce;
  --royal:#0a64bc;
  --navy:#0b1a38;
  --navy-deep:#071229;
  --ink:#1d2740;
  --muted:#6b7385;
  --paper:#ffffff;
  --mist:#e9edf2;
}
*{box-sizing:border-box;margin:0;padding:0}
html,body{width:1200px;height:3252px;overflow:hidden}
body{font-family:"Open Sans",Arial,sans-serif;color:var(--ink);background:var(--paper);position:relative}
h1,h2,h3,.nav,.btn,.stat,.brand{font-family:"IBM Plex Sans",Arial,sans-serif}
section,header,footer{position:absolute;left:0;width:1200px;overflow:hidden}
.btn{display:inline-block;border-radius:30px;font-size:13px;font-weight:500;padding:9px 24px;text-decoration:none;line-height:1;white-space:nowrap}
.btn-fill{background:var(--brand);color:#fff}
.btn-line{border:1.5px solid var(--brand);color:var(--brand)}
.btn-white-line{border:1.5px solid #fff;color:#fff}
.btn-white{background:#fff;color:var(--royal)}

/* hero */
.hero{top:0;height:600px;background:linear-gradient(120deg,#2a3c5e 0%,#1c2c4d 45%,#12224a 100%)}
.hero-photo{position:absolute;inset:0;background:radial-gradient(circle at 70% 40%,rgba(120,140,170,.35),transparent 60%)}
.hero-shapes{position:absolute;inset:0}
.brand{position:absolute;left:48px;top:38px;font-size:19px;font-weight:700;color:#fff;white-space:nowrap}
.nav{position:absolute;top:0;left:0;width:1200px;height:90px;font-size:13px;color:#fff;white-space:nowrap}
.nav span,.nav a{position:absolute;top:40px}
.nav .active{top:0;left:410px;background:var(--brand);padding:40px 20px 12px;border-radius:0 0 14px 14px}
.nav .book{top:32px;left:944px;padding:10px 22px}
.hero h1{position:absolute;left:56px;top:262px;width:560px;font-size:36px;line-height:1.22;font-weight:700;color:#fff}
.hero .hero-cta{position:absolute;left:56px;top:470px;font-size:12px;padding:8px 20px}

/* stats */
.stats{top:600px;height:112px;background:var(--navy);display:flex}
.stat{flex:1;display:flex;flex-direction:column;align-items:center;justify-content:center;gap:8px;color:#dfe7f3;font-size:13px;border-right:1px solid rgba(255,255,255,.08)}
.stat:last-child{border:none}

/* about */
.about{top:712px;height:600px}
.about-text{position:absolute;left:56px;top:120px;width:480px}
.about h2{font-size:32px;font-weight:600;color:var(--navy)}
.about h2 span{color:var(--brand)}
.about p{margin-top:18px;font-size:12.5px;line-height:1.75;color:var(--muted)}
.about .btn{margin-top:40px;font-size:12px;padding:8px 22px}
.about-photo{position:absolute;left:600px;top:28px;width:600px;height:572px;background:linear-gradient(135deg,#e8e6e2,#b9b6b0 55%,#7d7a76)}

/* solutions */
.solutions{top:1312px;height:600px;background:var(--brand)}
.col{position:absolute;top:20px;width:304px;color:#fff}
.col .shot{height:208px;background:linear-gradient(135deg,#dfe6ee,#9aabbf)}
.col:nth-child(2) .shot{background:linear-gradient(135deg,#f2f5f8,#b4c6d8)}
.col:nth-child(3) .shot{background:linear-gradient(135deg,#5c5a5a,#23252b)}
.col h3{margin-top:22px;font-size:15px;line-height:1.35;font-weight:700;text-transform:uppercase}
.col ul{list-style:none;margin-top:14px}
.col li{display:flex;align-items:center;gap:10px;font-size:12.5px;line-height:2}
.col .btn{position:absolute;top:470px;left:0;font-size:12px;padding:8px 20px}

/* cta */
.cta{top:1912px;height:400px}
.cta-photo{position:absolute;left:0;top:0;width:600px;height:400px;background:linear-gradient(135deg,#d7a26a,#8b5a33 60%,#3b2a22)}
.cta h2{position:absolute;left:700px;top:62px;width:420px;font-size:36px;line-height:1.22;font-weight:500;color:var(--navy)}
.cta h2 b{color:var(--royal);font-weight:700}
.cta .actions{position:absolute;left:700px;top:330px;display:flex;gap:14px}

/* estimate */
.estimate{top:2312px;height:520px;background:var(--mist)}
.estimate svg{position:absolute;inset:0}
.estimate h2{position:absolute;top:110px;width:100%;text-align:center;font-size:32px;font-weight:600;color:#fff}
.form{position:absolute;left:192px;top:238px;width:816px}
.row{display:flex;gap:20px}
.field{flex:1;height:34px;background:#fff;font-size:11px;color:var(--muted);padding:10px 14px}
.message{margin-top:22px;height:112px;background:#fff;font-size:11px;color:var(--muted);padding:12px 14px}
.submit{display:block;margin:28px auto 0;width:90px;text-align:center;border:1.5px solid #fff;color:#fff;font-size:12px;padding:7px 0}

/* footer */
.site-footer{top:2832px;height:420px;background:var(--navy-deep);color:#c9d3e2}
.f-brand{position:absolute;left:96px;top:56px;font-family:"IBM Plex Sans",Arial,sans-serif;font-size:27px;font-weight:700;color:#fff}
.social{position:absolute;left:96px;top:150px;display:flex;gap:14px}
.social span{width:28px;height:28px;border-radius:50%;background:var(--royal)}
.social span:nth-child(2){background:var(--brand)}
.f-col{position:absolute;top:60px;font-size:12.5px;line-height:1.7}
.f-col h3{font-size:17px;color:#fff;font-weight:600;margin-bottom:22px}
.f-col .phone{font-size:18px;color:#fff}
.f-contact{left:450px;width:280px}
.f-sign{left:800px;width:300px}
.sign-form{display:flex;gap:10px;margin-top:24px}
.sign-form .input{flex:1;border:1px solid rgba(255,255,255,.35);font-size:11px;padding:8px 12px;color:#95a3b8}
.sign-form .btn{border-radius:20px;font-size:12px}
.legal{position:absolute;left:96px;right:96px;top:368px;display:flex;font-size:12px;color:#9fabbd}
.legal span b{color:var(--brand);font-weight:400}
.legal .links{margin-left:360px;display:flex;gap:56px}
</style>
</head>
<body>

<header class="hero">
  <div class="hero-photo" role="img" aria-label="Photo of a business desk with finance papers under a dark blue overlay"></div>
  <svg class="hero-shapes" width="1200" height="600" viewBox="0 0 1200 600" aria-hidden="true">
    <polygon points="820,0 1200,0 1200,420 980,600 700,600 900,300" fill="#0a64bc" opacity=".35"/>
    <polygon points="1000,120 1200,0 1200,600 1040,600" fill="#0393ce" opacity=".3"/>
    <polygon points="560,600 760,360 900,600" fill="#0a1a3c" opacity=".45"/>
  </svg>
  <div class="brand">Tarnwell Ridge Capital</div>
  <nav class="nav">
    <span class="active">Home</span>
    <span style="left:500px">About Us</span>
    <span style="left:600px">Financing Solutions</span>
    <span style="left:748px">Contact</span>
    <span style="left:836px">Apply Now</span>
    <a class="btn btn-fill book">Book an Appointment</a>
  </nav>
  <h1>Tarnwell Ridge Capital brings global, regional and local experience in trade finance,</h1>
  <a class="btn btn-fill hero-cta">Contact Us</a>
</header>

<section class="stats">
  <div class="stat">
    <svg width="26" height="26" viewBox="0 0 26 26" aria-hidden="true"><circle cx="13" cy="13" r="11" fill="none" stroke="#0393ce" stroke-width="2"/><path d="M13 7v12M9 10h6a2 2 0 010 4h-4a2 2 0 000 4h6" fill="none" stroke="#0393ce" stroke-width="1.6"/></svg>
    Over $1.2B invested by our partners
  </div>
  <div class="stat">
    <svg width="26" height="26" viewBox="0 0 26 26" aria-hidden="true"><path d="M4 22V12M11 22V6M18 22V14" stroke="#0393ce" stroke-width="3"/></svg>
    50+ life science and technology investments
  </div>
  <div class="stat">
    <svg width="26" height="26" viewBox="0 0 26 26" aria-hidden="true"><circle cx="13" cy="13" r="11" fill="none" stroke="#0393ce" stroke-width="2"/><path d="M13 7v6l4 3" fill="none" stroke="#0393ce" stroke-width="2"/></svg>
    Over a decade innovating financing structures
  </div>
</section>

<section class="about">
  <div class="about-text">
    <h2>About <span>Tarnwell Ridge Capital</span></h2>
    <p>Tarnwell Ridge Capital was created by its founder and CEO, with a passion for helping companies raise the working capital they need to grow, through trusted funding structures, clear advice and long term partners in every market.</p>
    <p>Tarnwell Ridge Capital brings global, regional and local experience in trade finance, supply chain finance and commodity finance.</p>
    <a class="btn btn-line">Explore More</a>
  </div>
  <div class="about-photo" role="img" aria-label="Photo of hands working with a calculator and financial reports on a desk"></div>
</section>

<section class="solutions">
  <div class="col" style="left:96px">
    <div class="shot" role="img" aria-label="Photo of a laptop showing financial charts"></div>
    <h3>Financing solutions that will be provided by Tarnwell Ridge Capital will include:</h3>
    <ul>
      <li><svg width="12" height="12" viewBox="0 0 12 12"><circle cx="6" cy="6" r="5.3" fill="none" stroke="#fff"/><path d="M3.5 6l1.8 1.8L8.6 4.4" fill="none" stroke="#fff"/></svg>Receivables Finance, which include:</li>
      <li><svg width="12" height="12" viewBox="0 0 12 12"><circle cx="6" cy="6" r="5.3" fill="none" stroke="#fff"/><path d="M3.5 6l1.8 1.8L8.6 4.4" fill="none" stroke="#fff"/></svg>Receivables Financing</li>
      <li><svg width="12" height="12" viewBox="0 0 12 12"><circle cx="6" cy="6" r="5.3" fill="none" stroke="#fff"/><path d="M3.5 6l1.8 1.8L8.6 4.4" fill="none" stroke="#fff"/></svg>Factoring</li>
      <li><svg width="12" height="12" viewBox="0 0 12 12"><circle cx="6" cy="6" r="5.3" fill="none" stroke="#fff"/><path d="M3.5 6l1.8 1.8L8.6 4.4" fill="none" stroke="#fff"/></svg>Invoice Financing</li>
    </ul>
    <a class="btn btn-white-line">Read More</a>
  </div>
  <div class="col" style="left:448px">
    <div class="shot" role="img" aria-label="Photo of printed bar charts and financial graphs"></div>
    <h3>The financing solutions mentioned above will assist businesses to:</h3>
    <ul>
      <li><svg width="12" height="12" viewBox="0 0 12 12"><circle cx="6" cy="6" r="5.3" fill="none" stroke="#fff"/><path d="M3.5 6l1.8 1.8L8.6 4.4" fill="none" stroke="#fff"/></svg>Monetise its receivables to accelerate its cash cycle</li>
      <li><svg width="12" height="12" viewBox="0 0 12 12"><circle cx="6" cy="6" r="5.3" fill="none" stroke="#fff"/><path d="M3.5 6l1.8 1.8L8.6 4.4" fill="none" stroke="#fff"/></svg>Mitigate debtor credit risk</li>
      <li><svg width="12" height="12" viewBox="0 0 12 12"><circle cx="6" cy="6" r="5.3" fill="none" stroke="#fff"/><path d="M3.5 6l1.8 1.8L8.6 4.4" fill="none" stroke="#fff"/></svg>Renovate payment risks</li>
    </ul>
    <a class="btn btn-white">Read More</a>
  </div>
  <div class="col" style="left:800px">
    <div class="shot" role="img" aria-label="Photo of business people reviewing documents at a table"></div>
    <h3>The industry sectors focused on are, but not limited to:</h3>
    <ul>
      <li><svg width="12" height="12" viewBox="0 0 12 12"><circle cx="6" cy="6" r="5.3" fill="none" stroke="#fff"/><path d="M3.5 6l1.8 1.8L8.6 4.4" fill="none" stroke="#fff"/></svg>Infrastructure</li>
      <li><svg width="12" height="12" viewBox="0 0 12 12"><circle cx="6" cy="6" r="5.3" fill="none" stroke="#fff"/><path d="M3.5 6l1.8 1.8L8.6 4.4" fill="none" stroke="#fff"/></svg>Resources</li>
      <li><svg width="12" height="12" viewBox="0 0 12 12"><circle cx="6" cy="6" r="5.3" fill="none" stroke="#fff"/><path d="M3.5 6l1.8 1.8L8.6 4.4" fill="none" stroke="#fff"/></svg>FMCG</li>
      <li><svg width="12" height="12" viewBox="0 0 12 12"><circle cx="6" cy="6" r="5.3" fill="none" stroke="#fff"/><path d="M3.5 6l1.8 1.8L8.6 4.4" fill="none" stroke="#fff"/></svg>Industrial</li>
      <li><svg width="12" height="12" viewBox="0 0 12 12"><circle cx="6" cy="6" r="5.3" fill="none" stroke="#fff"/><path d="M3.5 6l1.8 1.8L8.6 4.4" fill="none" stroke="#fff"/></svg>Services</li>
    </ul>
    <a class="btn btn-white-line">Read More</a>
  </div>
</section>

<section class="cta">
  <div class="cta-photo" role="img" aria-label="Photo of a person using a calculator beside a laptop in warm light"></div>
  <h2>We look forward to providing <b>financing solutions</b> that will answer your working capital needs.</h2>
  <div class="actions">
    <a class="btn btn-line">Apply Now</a>
    <a class="btn btn-fill">Book an Appointment</a>
  </div>
</section>

<section class="estimate">
  <svg width="1200" height="520" viewBox="0 0 1200 520" aria-hidden="true">
    <polygon points="0,0 760,0 600,520 0,520" fill="#0393ce"/>
    <polygon points="760,0 1200,0 1200,520 600,520" fill="#8d96a3"/>
    <polygon points="960,0 1200,0 1200,300" fill="#b4bcc6"/>
    <polygon points="0,300 260,520 0,520" fill="#0a64bc"/>
  </svg>
  <h2>Get a Free Estimate</h2>
  <div class="form">
    <div class="row">
      <div class="field">Your Name</div>
      <div class="field">Email</div>
      <div class="field">Phone</div>
    </div>
    <div class="message">Message</div>
    <a class="submit btn">Submit</a>
  </div>
</section>

<footer class="site-footer">
  <div class="f-brand">Tarnwell Ridge Capital</div>
  <div class="social" aria-label="Social links"><span></span><span></span><span></span></div>
  <div class="f-col f-contact">
    <h3>Contact Info</h3>
    <div class="phone">Call Us: +1 (416) 555-0148</div>
    <div>info@tarnwellridge.ca</div>
    <div style="margin-top:14px">Address:<br>Suite 4, 118 Harbourline Road,<br>Halden NSW 2031 Australia</div>
  </div>
  <div class="f-col f-sign">
    <h3>Sign Up</h3>
    <div>Get our latest insights and news delivered by Tarnwell Ridge Capital</div>
    <div class="sign-form"><span class="input">Your Email...</span><a class="btn btn-fill">Sign Up</a></div>
  </div>
  <div class="legal">
    <span>© 2021 <b>Tarnwell Ridge Capital</b>. All Right Reserved</span>
    <div class="links"><span>T&amp;C's</span><span>Privacy Policy</span></div>
  </div>
</footer>

</body>
</html>
```